Process Diagram - Circular Economy

I would like for a designer to take this rough sketch and turn it into a high quality design which can be used in a business presentation. Seeking to get both PDF and Jpeg file versions of the finished product.

Colours don't have to be the exact same as the rough sketch PDF, the green used is pretty ugly so open to some changes.

Target Market(s)

Corporate audience

Requirements
Must have
• Clear text for each party; VENOR, QUELDRA, BUYER

Smaller text for the functions; marketing, recovery, logistics, cleaning, decontamination, testing & re-certification, storage, engineering suitability

```html
<!DOCTYPE html>
<html lang="en">
<head>
<meta charset="utf-8">
<title>Circular Economy Process</title>
<link href="https://fonts.googleapis.com/css2?family=Open+Sans:wght@600;700&display=swap" rel="stylesheet">
<style>
  :root {
    --bg: #ffffff;
    --ink: #333333;
    --label: #ffffff;
    --gap: #ffffff;
    --red-a: #b80000;   --red-b: #e01212;
    --orange-a: #ff4400; --orange-b: #ff7414;
    --amber-a: #f29e00; --amber-b: #ffc80a;
    --green-a: #5f9e00; --green-b: #94c400;
    --cyan-a: #009fd0;  --cyan-b: #1ac6e6;
    --navy-a: #0c4894;  --navy-b: #1c70bd;
    --violet-a: #640888; --violet-b: #9414ac;
  }
  html, body {
    margin: 0;
    padding: 0;
    width: 1200px;
    height: 1200px;
    overflow: hidden;
    background: var(--bg);
  }
  .canvas {
    width: 1200px;
    height: 1200px;
    display: block;
  }
  .stage {
    stroke: var(--gap);
    stroke-width: 9;
    stroke-linejoin: miter;
  }
  .stage-label {
    font-family: "Open Sans", sans-serif;
    font-weight: 700;
    fill: var(--label);
    text-anchor: middle;
    dominant-baseline: middle;
  }
  .party { font-size: 44px; letter-spacing: 1px; }
  .hub { font-size: 42px; letter-spacing: 0.5px; }
  .function { font-size: 34px; }
  .function-sm { font-size: 27px; }
  .function-xs { font-size: 23px; }
  .milestone {
    font-family: "Open Sans", sans-serif;
    font-weight: 700;
    font-size: 42px;
    fill: var(--ink);
    text-anchor: middle;
  }
</style>
</head>
<body>
<svg class="canvas" viewBox="0 0 1500 1500" xmlns="http://www.w3.org/2000/svg" role="img" aria-label="Circular economy process from end of life at the vendor to new life at the buyer">
  <defs>
    <radialGradient id="grad-red" cx="50%" cy="45%" r="70%"><stop offset="0" stop-color="var(--red-b)"/><stop offset="1" stop-color="var(--red-a)"/></radialGradient>
    <radialGradient id="grad-orange" cx="50%" cy="45%" r="70%"><stop offset="0" stop-color="var(--orange-b)"/><stop offset="1" stop-color="var(--orange-a)"/></radialGradient>
    <radialGradient id="grad-amber" cx="50%" cy="50%" r="70%"><stop offset="0" stop-color="var(--amber-b)"/><stop offset="1" stop-color="var(--amber-a)"/></radialGradient>
    <radialGradient id="grad-green" cx="45%" cy="50%" r="70%"><stop offset="0" stop-color="var(--green-b)"/><stop offset="1" stop-color="var(--green-a)"/></radialGradient>
    <radialGradient id="grad-cyan" cx="50%" cy="50%" r="70%"><stop offset="0" stop-color="var(--cyan-b)"/><stop offset="1" stop-color="var(--cyan-a)"/></radialGradient>
    <radialGradient id="grad-navy" cx="55%" cy="40%" r="75%"><stop offset="0" stop-color="var(--navy-b)"/><stop offset="1" stop-color="var(--navy-a)"/></radialGradient>
    <radialGradient id="grad-violet" cx="50%" cy="40%" r="75%"><stop offset="0" stop-color="var(--violet-b)"/><stop offset="1" stop-color="var(--violet-a)"/></radialGradient>
    <filter id="soft-shadow" x="-10%" y="-10%" width="120%" height="120%">
      <feDropShadow dx="2" dy="4" stdDeviation="4" flood-color="#000" flood-opacity="0.28"/>
    </filter>
    <filter id="text-shadow" x="-10%" y="-30%" width="120%" height="160%">
      <feDropShadow dx="1.5" dy="1.5" stdDeviation="1" flood-color="#000" flood-opacity="0.35"/>
    </filter>
  </defs>

  <g class="flow" filter="url(#soft-shadow)">
    <path class="stage stage-vendor" fill="url(#grad-red)" d="M272,910 L382,855 L492,910 L492,1027 L272,1027 Z"/>
    <path class="stage stage-recovery" fill="url(#grad-orange)" d="M272,700 L382,650 L492,700 L492,910 L382,855 L272,910 Z"/>
    <path class="stage stage-logistics" fill="url(#grad-amber)" d="M272,700 L272,659 A294,294 0 0 1 455,387 L566,470 L566,585 A74,74 0 0 0 492,659 L492,700 L382,650 Z"/>
    <path class="stage stage-cleaning" fill="url(#grad-green)" d="M455,387 A294,294 0 0 1 860,659 L750,705 L640,659 A74,74 0 0 0 566,585 L566,470 Z"/>
    <path class="stage stage-hub" fill="url(#grad-cyan)" d="M640,659 L750,705 L860,659 L860,830 L750,875 L640,830 Z"/>
    <path class="stage stage-decontamination" fill="url(#grad-navy)" d="M640,830 L750,875 L860,830 L860,841 A74,74 0 0 0 895,905 L862,1010 L730,1052 A294,294 0 0 1 640,841 Z"/>
    <path class="stage stage-testing" fill="url(#grad-violet)" d="M895,905 A74,74 0 0 0 965,910 L1052,978 L1052,1112 A294,294 0 0 1 730,1052 L862,1010 Z"/>
    <path class="stage stage-storage" fill="url(#grad-red)" d="M965,910 A74,74 0 0 0 1007,855 L1117,812 L1228,855 A294,294 0 0 1 1052,1112 L1052,978 Z"/>
    <path class="stage stage-engineering" fill="url(#grad-orange)" d="M1007,855 L1007,688 L1117,640 L1228,688 L1228,855 L1117,812 Z"/>
    <path class="stage stage-buyer" fill="url(#grad-amber)" d="M1007,688 L1007,473 L1228,473 L1228,688 L1117,640 Z"/>
  </g>

  <g class="labels" filter="url(#text-shadow)">
    <text class="stage-label party" x="380" y="958">VENDOR</text>
    <text class="stage-label function" x="380" y="766">Recovery</text>
    <text class="stage-label function" x="422" y="538">Logistics</text>
    <text class="stage-label function" x="700" y="538">Cleaning</text>
    <text class="stage-label hub" x="750" y="767">QUELDRA</text>
    <text class="stage-label function-xs" x="766" y="920">Decontamination</text>
    <text class="stage-label function-xs" x="937" y="999">Testing</text>
    <text class="stage-label function-xs" x="937" y="1032">&amp;</text>
    <text class="stage-label function-xs" x="940" y="1066">Re-certification</text>
    <text class="stage-label function" x="1112" y="902">Storage</text>
    <text class="stage-label function-sm" x="1122" y="722">Engineering</text>
    <text class="stage-label function-sm" x="1122" y="760">Suitability</text>
    <text class="stage-label party" x="1122" y="556">BUYER</text>
  </g>

  <text class="milestone" x="1119" y="428">New Life</text>
  <text class="milestone" x="387" y="1091">End of Life</text>
</svg>
</body>
</html>
```